Brisken. business card

We need a business card design for a new mobile car-wash catered toward urban residents. The use of colour should be black, white and red and should be sleek and minimal. The final design should be modern and enticing to look at. A picture of the logo is attached. The font and design should resemble something similar to the logo.

```html
<!DOCTYPE html>
<html lang="en">
<head>
<meta charset="utf-8">
<title>Brisken. Business Card</title>
<link rel="stylesheet" href="https://fonts.googleapis.com/css2?family=Michroma&family=Montserrat:ital,wght@0,400;0,600;0,700;1,700&display=swap">
<style>
  :root {
    --canvas: #ececec;
    --paper: #ffffff;
    --ink-black: #0d0d0d;
    --ink-dark: #1c1c1c;
    --brand-red: #c4262e;
    --brand-red-fade: rgba(196, 38, 46, 0);
    --text-grey: #6f6f6f;
    --text-light: #9a9a9a;
    --brand-white: #f4f4f4;
  }
  * { margin: 0; padding: 0; box-sizing: border-box; }
  html, body {
    width: 1200px;
    height: 1000px;
    overflow: hidden;
    background: var(--canvas);
  }
  .sheet {
    position: relative;
    width: 1200px;
    height: 1000px;
    display: flex;
    flex-direction: column;
    align-items: center;
    justify-content: center;
    gap: 60px;
  }
  .card {
    position: relative;
    width: 600px;
    height: 343px;
    box-shadow: 0 10px 30px rgba(0, 0, 0, 0.15);
    overflow: hidden;
  }

  /* Back: contact side */
  .card--back { background: var(--paper); }
  .card__accent {
    position: absolute;
    left: 150px;
    top: 42px;
    width: 220px;
    height: 56px;
    background: linear-gradient(90deg, var(--brand-red) 0%, var(--brand-red) 35%, var(--brand-red-fade) 100%);
  }
  .card__rule {
    position: absolute;
    left: 160px;
    top: 138px;
    width: 3px;
    height: 130px;
    background: var(--brand-red);
  }
  .contact {
    position: absolute;
    left: 205px;
    top: 122px;
    width: 370px;
    font-family: "Montserrat", sans-serif;
    color: var(--text-grey);
  }
  .contact__name {
    font-family: "Michroma", sans-serif;
    font-weight: 400;
    font-size: 17px;
    letter-spacing: 2px;
    color: var(--brand-red);
    text-transform: uppercase;
    line-height: 1.1;
    white-space: nowrap;
  }
  .contact__position {
    font-size: 11px;
    font-weight: 700;
    font-style: italic;
    letter-spacing: 1px;
    text-transform: uppercase;
    margin-top: 4px;
  }
  .contact__company {
    font-size: 11px;
    font-weight: 700;
    letter-spacing: 1.5px;
    text-transform: uppercase;
    margin-top: 1px;
  }
  .contact__lines {
    list-style: none;
    margin-top: 14px;
    font-size: 11px;
    line-height: 1.25;
  }
  .contact__lines b { font-weight: 700; }
  .contact__address {
    margin-top: 12px;
    font-size: 10.5px;
    color: var(--text-light);
    letter-spacing: 0.3px;
    white-space: nowrap;
  }

  /* Front: brand side */
  .card--front {
    background: radial-gradient(ellipse at 50% 50%, #2a2a2a 0%, var(--ink-dark) 40%, var(--ink-black) 100%);
    display: flex;
    align-items: center;
    justify-content: center;
  }
  .brand {
    display: flex;
    align-items: center;
    gap: 12px;
  }
  .brand__dot {
    width: 14px;
    height: 14px;
    border-radius: 50%;
    background: var(--brand-red);
  }
  .brand__name {
    font-family: "Montserrat", sans-serif;
    font-weight: 700;
    font-size: 40px;
    letter-spacing: 4px;
    color: var(--brand-white);
    text-transform: uppercase;
  }
</style>
</head>
<body>
<main class="sheet">
  <section class="card card--back" aria-label="Business card, contact side">
    <div class="card__accent" role="img" aria-label="Red angular accent ornament"></div>
    <div class="card__rule"></div>
    <div class="contact">
      <h1 class="contact__name">Name Lastname</h1>
      <p class="contact__position">Position</p>
      <p class="contact__company">Brisken Car Wash</p>
      <ul class="contact__lines">
        <li><b>Phone:</b> +XX XXX XXX XXX</li>
        <li><b>Mobile:</b> +XX XXX XXX XXX</li>
        <li><b>Email:</b> Name@email.com</li>
        <li><b>Web:</b> www.website.com</li>
      </ul>
      <p class="contact__address">P.O Box XXX, Suburb State CODE, Country</p>
    </div>
  </section>

  <section class="card card--front" aria-label="Business card, brand side">
    <div class="brand">
      <span class="brand__dot"></span>
      <span class="brand__name">Brisken.</span>
    </div>
  </section>
</main>
</body>
</html>
```